Nova crest cleansers Trading L.L.C

We need stationary design for our new company contain ( Business card - head latter - envelops( big & small) - folder file ) One identity and creative design & has related with logo colors ....A unified identity
The main elements of the design that includes the main logos (logo crest + crest logo membership Khalid bin Nasser) as it is in the attachment then the address of the company.
The Address is
Ras Hamdan - Next to Corniche Plaza Mall
Noor Trade Tower Building - 604
P.O.Box : 47819 Dubai - U.A.E
Tel. : 00971 4 58 71 204
Fax : 00971 4 58 71 205
Email : info@novacrestcleansers.example
www.novacrestcleansers.example
Please read the attachment in an important way, especially the terms of the government logo (Khalid Bin Nasser Membership)
In the design of business cards .. Please put slogans (Oru fresh home - Oru Professional - Faraheed ) be in the back of the card
Put my name sample
Samir Youssef Abdul Karim
Director Manager
Mobil : + 971 52 387 0 387

```html
<!DOCTYPE html>
<html lang="en">
<head>
<meta charset="utf-8">
<title>Nova crest cleansers Trading L.L.C — Stationery</title>
<link href="https://fonts.googleapis.com/css2?family=Montserrat:wght@400;500;700&family=Arimo:wght@400;700&display=swap" rel="stylesheet">
<style>
  :root {
    --bg: #dcdcdc;
    --paper: #f7f7f7;
    --red: #e8212a;
    --red-line: #f0585e;
    --ink: #222222;
    --ink-soft: #555555;
    --brand-green: #5aa83a;
    --brand-blue: #1f7fc0;
    --white: #ffffff;
  }
  * { box-sizing: border-box; margin: 0; padding: 0; }
  html, body { width: 1200px; height: 1200px; overflow: hidden; }
  body {
    background: var(--bg);
    position: relative;
    font-family: "Montserrat", sans-serif;
    color: var(--ink);
  }
  .sheet {
    position: absolute;
    background: var(--paper);
    box-shadow: 0 2px 6px rgba(0,0,0,0.12);
    overflow: hidden;
  }
  .rule-v, .rule-h { position: absolute; }
  .rule-v {
    width: 7px; top: 0; bottom: 0;
    background: linear-gradient(to right, var(--c) 0 1px, transparent 1px 3px, var(--c) 3px 4px, transparent 4px 6px, var(--c) 6px 7px);
  }
  .rule-h {
    height: 7px; left: 0; right: 0;
    background: linear-gradient(to bottom, var(--c) 0 1px, transparent 1px 3px, var(--c) 3px 4px, transparent 4px 6px, var(--c) 6px 7px);
  }
  .on-paper { --c: var(--red-line); }
  .on-red { --c: rgba(255,255,255,0.85); }

  .membership {
    position: absolute;
    font-family: "Montserrat", sans-serif;
    font-weight: 700;
    color: var(--red);
    white-space: nowrap;
    letter-spacing: 0.01em;
  }

  /* Envelope */
  .envelope { left: 60px; top: 60px; width: 620px; height: 300px; }
  .envelope .rule-v { left: 48px; }
  .envelope .rule-h { top: 250px; }
  .envelope .membership { right: 40px; top: 214px; font-size: 17px; }

  /* Letterhead */
  .letterhead { left: 60px; top: 410px; width: 560px; height: 760px; }
  .letterhead .rule-v { left: 56px; }
  .letterhead .rule-h { top: 650px; }
  .letterhead .membership { right: 40px; top: 40px; font-size: 16px; }
  .letter-date { position: absolute; right: 40px; top: 92px; font-family: "Arimo", sans-serif; font-size: 9px; }
  .letter-date b { font-weight: 700; margin-right: 4px; }
  .letter-body {
    position: absolute; left: 96px; right: 44px; top: 140px;
    font-family: "Arimo", sans-serif; font-size: 8.6px; line-height: 1.32; color: var(--ink);
  }
  .letter-body p { margin-bottom: 11px; }
  .letter-sign { margin-top: 26px; }
  .letter-sign .name { margin-top: 16px; }
  .company-mark {
    position: absolute; right: 44px; top: 596px;
    display: flex; align-items: center; gap: 8px;
    font-family: "Montserrat", sans-serif; font-weight: 500; font-size: 19px; color: var(--brand-blue);
  }
  .company-mark .dot { width: 20px; height: 20px; border-radius: 50%; background: var(--brand-green); }
  .letter-footer {
    position: absolute; left: 96px; right: 30px; top: 676px;
    display: flex; align-items: flex-start; gap: 14px;
    font-size: 7.4px; line-height: 1.45; color: var(--ink-soft);
  }
  .letter-footer .col + .col { border-left: 1px solid var(--ink); padding-left: 14px; }

  /* Business cards */
  .card { width: 420px; height: 240px; }
  .card-back { left: 720px; top: 410px; }
  .card-front { left: 720px; top: 700px; background: var(--red); }
  .card .rule-v { left: 30px; }
  .card .rule-h { top: 196px; }
  .card-back .membership { right: 26px; top: 164px; font-size: 12px; }
  .brand-row {
    position: absolute; left: 64px; right: 26px; top: 36px;
    display: flex; justify-content: space-between;
  }
  .brand { display: flex; flex-direction: column; align-items: center; gap: 6px; font-size: 8px; color: var(--ink-soft); }
  .brand .badge { width: 34px; height: 22px; border-radius: 3px; }
  .badge.green { background: var(--brand-green); }
  .badge.red { background: var(--red); }
  .badge.blue { background: var(--brand-blue); }
  .card-front .holder {
    position: absolute; right: 28px; top: 30px; text-align: left;
    color: var(--white); font-size: 9.5px; line-height: 1.45;
  }
  .card-front .membership { color: var(--white); right: 26px; top: 164px; font-size: 12px; }
</style>
</head>
<body>

  <section class="sheet envelope" aria-label="Envelope">
    <div class="rule-v on-paper"></div>
    <div class="rule-h on-paper"></div>
    <div class="membership">Khalid Bin Nasser Membership</div>
  </section>

  <section class="sheet letterhead" aria-label="Letterhead">
    <div class="rule-v on-paper"></div>
    <div class="rule-h on-paper"></div>
    <div class="membership">Khalid Bin Nasser Membership</div>
    <div class="letter-date"><b>Date:</b>30 Dec 2017</div>
    <div class="letter-body">
      <p>Dear<br>Mr. Rowan Ellis<br>12-3, Harbour Lane,<br>Singapore 408812</p>
      <p>Lorem ipsum dolor sit amet, consectetur adipisicing elit, sed do eiusmod tempor incididunt ut labore et dolore magna aliqua. Ut enim ad minim veniam, quis nostrud exercitation ullamco laboris nisi ut aliquip ex ea commodo consequat. Duis aute irure dolor in reprehenderit in voluptate velit esse cillum dolore eu fugiat nulla pariatur. Excepteur sint occaecat cupidatat non proident, sunt in culpa qui officia deserunt mollit anim id est laborum.</p>
      <p>Lorem ipsum dolor sit amet, consectetur adipisicing elit, sed do eiusmod tempor incididunt ut labore et dolore magna aliqua. Ut enim ad minim veniam, quis nostrud exercitation ullamco laboris nisi ut aliquip ex ea commodo consequat. Excepteur sint occaecat cupidatat non proident, sunt in culpa qui officia deserunt mollit anim id est laborum. Lorem ipsum dolor sit amet, consectetur adipisicing elit, sed do eiusmod tempor incididunt ut labore et dolore magna aliqua. Ut enim ad minim veniam, quis nostrud exercitation ullamco laboris nisi ut aliquip ex ea commodo consequat.</p>
      <p>Excepteur sint occaecat cupidatat non proident, sunt in culpa qui officia deserunt mollit anim id est laborum. Lorem ipsum dolor sit amet, consectetur adipisicing elit, sed do eiusmod oris nisi ut aliquip ex ea commodo consequat. Duis aute irure dolor in reprehenderit in voluptate velit esse cillum dolore eu fugiat nulla pariat oris nisi ut aliquip ex ea commodo consequat. Duis aute irure dolor in reprehendent in voluptate velit tempor incididunt ut labore et dolore magna aliqua.</p>
      <div class="letter-sign">
        <p>Best regards,</p>
        <p class="name">Daniel Hart<br>Executive Director</p>
      </div>
    </div>
    <div class="company-mark"><span class="dot"></span>Nova crest</div>
    <div class="letter-footer">
      <div class="col">Ras Hamdan - Next to Corniche Plaza Mall<br>Noor Trade Tower Building - 604<br>P.O.Box : 47819 Dubai - U.A.E</div>
      <div class="col">Tel. : 00971 4 58 71 204<br>Fax : 00971 4 58 71 205</div>
      <div class="col">Email : info@novacrestcleansers.example<br>www.novacrestcleansers.example</div>
    </div>
  </section>

  <section class="sheet card card-back" aria-label="Business card back">
    <div class="rule-v on-paper"></div>
    <div class="rule-h on-paper"></div>
    <div class="brand-row">
      <div class="brand"><span class="badge green"></span>Oru fresh home</div>
      <div class="brand"><span class="badge red"></span>Oru Professional</div>
      <div class="brand"><span class="badge blue"></span>Faraheed</div>
    </div>
    <div class="membership">Khalid Bin Nasser Membership</div>
  </section>

  <section class="sheet card card-front" aria-label="Business card front">
    <div class="rule-v on-red"></div>
    <div class="rule-h on-red"></div>
    <div class="holder">Samir Youssef Abdul Karim<br>Director Manager<br>Mobil : + 971 52 387 0 387</div>
    <div class="membership">Khalid Bin Nasser Membership</div>
  </section>

</body>
</html>
```